QR-482 Horizons, LLC business cards
Personal Fitness Training
Professional
QR 482 Horizons, LLC
Fitness Solutions
based out of Miami but want to train internationally over the net
bellamorvain@qr482.net
www.qr482.net
K20000047153
I would also like to list my bellamorvain@zentmail.net email
I will be based out of the Miami area but do not have an exact location for the address.
Contact for your Free Fitness Assessment
415 263 9071 or bellamorvain@qr482.net

```html
<!DOCTYPE html>
<html lang="en">
<head>
<meta charset="utf-8">
<title>QR-482 Horizons, LLC business cards</title>
<link rel="stylesheet" href="https://fonts.googleapis.com/css2?family=Open+Sans:ital,wght@0,400;0,600;0,700;1,600;1,700&display=swap">
<style>
  :root {
    --backdrop: #8a8a8a;
    --card-light: #ffffff;
    --card-dark: #000000;
    --brand-red: #d3151c;
    --text-gray: #555555;
    --rule-gray: #b8b8b8;
    --text-white: #ffffff;
  }
  * { margin: 0; padding: 0; box-sizing: border-box; }
  html, body { width: 1200px; height: 901px; overflow: hidden; }
  body {
    background: var(--backdrop);
    font-family: "Open Sans", sans-serif;
    position: relative;
  }
  .card {
    position: absolute;
    left: 268px;
    width: 667px;
    box-shadow: 0 4px 14px rgba(0,0,0,0.35);
  }
  .card--front { top: 61px; height: 389px; background: var(--card-light); }
  .card--back { top: 470px; height: 382px; background: var(--card-dark); }

  .brand-mark {
    position: absolute;
    display: flex;
    align-items: center;
    gap: 14px;
  }
  .brand-mark__square {
    width: 58px; height: 58px;
    background: var(--brand-red);
  }
  .brand-mark__name {
    font-weight: 700;
    font-size: 50px;
    line-height: 1;
    color: var(--brand-red);
  }
  .card--front .brand-mark { left: 18px; top: 28px; }
  .card--back .brand-mark { left: 50%; top: 120px; transform: translateX(-50%); }

  .service-title {
    position: absolute;
    right: 26px; top: 92px;
    font-style: italic;
    font-weight: 600;
    font-size: 31px;
    color: var(--brand-red);
    white-space: nowrap;
  }
  .service-rule {
    position: absolute;
    left: 250px; right: 8px; top: 140px;
    height: 3px;
    background: var(--brand-red);
    border-bottom: 2px solid var(--rule-gray);
  }
  .trainer-name {
    position: absolute;
    right: 42px; top: 176px;
    font-size: 27px;
    color: var(--brand-red);
    white-space: nowrap;
  }
  .tagline {
    position: absolute;
    right: 56px; top: 210px;
    font-size: 16px;
    color: var(--text-gray);
    white-space: nowrap;
  }
  .contact-list {
    position: absolute;
    left: 12px; top: 266px;
    list-style: none;
    font-size: 18.5px;
    line-height: 29px;
    color: var(--text-gray);
  }
  .alt-email {
    position: absolute;
    right: 10px; top: 353px;
    font-size: 18.5px;
    color: var(--text-gray);
  }

  .offer {
    position: absolute;
    left: 0; right: 0; top: 250px;
    text-align: center;
    color: var(--text-white);
  }
  .offer__headline { font-size: 22px; }
  .offer__contact { font-size: 18.5px; margin-top: 8px; }
</style>
</head>
<body>
  <section class="card card--front" aria-label="Business card front">
    <div class="brand-mark">
      <span class="brand-mark__square"></span>
      <span class="brand-mark__name">QR-482</span>
    </div>
    <h1 class="service-title">Personal Fitness Training</h1>
    <div class="service-rule"></div>
    <p class="trainer-name">Bella Morvain</p>
    <p class="tagline">Look Better...Feel Better...Perform Better...</p>
    <ul class="contact-list">
      <li>Phone: 415 263 9071</li>
      <li>License No. K20000047153</li>
      <li>Website: www.qr482.net</li>
      <li>Email: bellamorvain@qr482.net</li>
    </ul>
    <p class="alt-email">bellamorvain@zentmail.net</p>
  </section>

  <section class="card card--back" aria-label="Business card back">
    <div class="brand-mark">
      <span class="brand-mark__square"></span>
      <span class="brand-mark__name">QR-482</span>
    </div>
    <div class="offer">
      <p class="offer__headline">Contact for your Free Fitness Assessment</p>
      <p class="offer__contact">415 263 9071 :: bellamorvain@qr482.net</p>
    </div>
  </section>
</body>
</html>
```